Design Tweak needed for a current site

Design on top of an existing quiz funnel

Ideally we would like to tweak what we have already built here (moving elements, styles, adding simple elements etc): http://offers.plumrivetdeals.com/can-you-save-on-car-insurance

The flow:
1) User lands on the quiz page
2) User answers X questions and moves through the flow
3) Calculating user results screen
4) User reaches a success screen, and is subsequently redirected

Keys to the design:
1) We need to emphasize the quiz title as that will drive engagement. In this case, this is a quiz to see if you might be eligible to save money on car insurance.

2) At the end of the quiz we need to make it very, very clear that the user is eligible for savings and that in order to complete the process they are being redirected to another page where they need to fill out a form. It is critical that the design communicates this very clearly... We can count down the time left until redirect and we can use any order of elements to make this point. I think our current design does a very bad job of this.

3) We want to have a "calculating" step so that it seems like the page is working in the background

Goals of the design:
1) Polished, high quality experience throughout
2) User is clearly prepared to be redirected to the conversion funnel/landing page at the end
3) User understands the value of completing the quiz

Target Market(s)

designers

Industry/Entity Type

Moving

Number of Pages Required

1 page

Font styles to use
Sans Serif

Colors

Designer to choose colors to be used in the design.

Requirements
Must have
• This quiz funnel is a template so while the current use case is for auto insurance, we would like a design that also would work in other contexts.
Should not have
• We don't want to materially change the core functionality of the quiz itself... redesigning any of the elements or interactions is encouraged though

```html
<!DOCTYPE html>
<html lang="en">
<head>
<meta charset="utf-8">
<title>Quiz: Are You Overpaying For Car Insurance? – PlumRivet</title>
<link href="https://fonts.googleapis.com/css2?family=Lato:wght@400;700&family=Open+Sans:wght@700&display=swap" rel="stylesheet">
<style>
  :root {
    --brand-blue: #1598d6;
    --brand-blue-dark: #0f86c4;
    --accent-yellow: #f5d80a;
    --ink: #262626;
    --track-grey: #c9c9c9;
    --stage-grey: #e8e8e8;
    --art-grey: #dcdcdc;
    --footer-grey: #424242;
    --white: #ffffff;
  }
  * { box-sizing: border-box; margin: 0; padding: 0; }
  html, body { width: 1200px; height: 679px; overflow: hidden; background: var(--white); }
  body { position: relative; font-family: "Lato", sans-serif; color: var(--ink); }

  .site-header {
    position: absolute; left: 0; top: 0; width: 1200px; height: 74px;
    background: var(--brand-blue);
    display: flex; align-items: center; justify-content: center; gap: 10px;
  }
  .brand-dot { width: 34px; height: 34px; border-radius: 50%; background: var(--white); }
  .brand-name { font-size: 34px; font-weight: 400; color: var(--white); letter-spacing: 0.2px; }

  .quiz-stage { position: absolute; left: 0; top: 74px; width: 1200px; height: 546px; overflow: hidden; }
  .stage-backdrop { position: absolute; left: 0; top: 0; }
  .hero-art {
    position: absolute; left: 694px; top: 153px; width: 476px; height: 194px;
    background: var(--art-grey); border-radius: 6px;
  }

  .quiz-panel { position: absolute; left: 99px; top: 0; width: 600px; }
  .quiz-title {
    position: absolute; top: 43px; left: 0; white-space: nowrap;
    font-size: 27.5px; font-weight: 700; color: var(--brand-blue);
  }
  .quiz-intro {
    position: absolute; top: 104px; left: 0; width: 560px;
    font-size: 15.5px; line-height: 26px; color: var(--ink);
  }
  .quiz-step { position: absolute; top: 185px; left: 0; font-size: 17px; font-weight: 400; }
  .progress-track {
    position: absolute; top: 225px; left: 0; width: 460px; height: 13px;
    background: var(--track-grey); border-radius: 7px; overflow: hidden;
  }
  .progress-fill {
    width: 323px; height: 100%; border-radius: 7px;
    background: repeating-linear-gradient(120deg, var(--brand-blue) 0 12px, #4bb3e6 12px 16px);
  }
  .quiz-question {
    position: absolute; top: 276px; left: -2px; white-space: nowrap;
    font-size: 23.5px; font-weight: 400;
  }
  .answer-options { position: absolute; top: 347px; left: 0; display: flex; gap: 48px; }
  .answer-option {
    width: 98px; display: flex; flex-direction: column; align-items: center;
    background: none; border: none; font-family: inherit; color: var(--ink); cursor: pointer;
  }
  .answer-badge {
    width: 98px; height: 98px; border-radius: 50%;
    background: var(--brand-blue); border: 3.5px solid var(--accent-yellow);
    display: flex; align-items: center; justify-content: center;
  }
  .answer-label { margin-top: 18px; font-size: 20.5px; font-weight: 400; }

  .site-footer {
    position: absolute; left: 0; top: 620px; width: 1200px; height: 59px;
    background: var(--footer-grey); color: var(--white);
    font-family: "Open Sans", sans-serif; font-weight: 700; font-size: 15.5px;
    display: flex; align-items: center; justify-content: center;
  }
  .page-code { position: absolute; right: 39px; }
</style>
</head>
<body>
  <header class="site-header">
    <span class="brand-dot"></span>
    <span class="brand-name">PlumRivet</span>
  </header>

  <main class="quiz-stage">
    <svg class="stage-backdrop" width="1200" height="546" aria-hidden="true">
      <circle cx="1023" cy="252" r="336" fill="var(--stage-grey)"/>
    </svg>
    <div class="hero-art" role="img" aria-label="Line drawing of a tow truck lifting a red car while a worried man looks on"></div>

    <section class="quiz-panel">
      <h1 class="quiz-title">Quiz: Are You Overpaying For Car Insurance?</h1>
      <p class="quiz-intro">Take our five question quiz to see if you might be eligible for car insurance savings.</p>
      <p class="quiz-step">Question 4/5</p>
      <div class="progress-track"><div class="progress-fill"></div></div>
      <h2 class="quiz-question">Have You Been In An Accident In The Last 12 Months?</h2>
      <div class="answer-options">
        <button class="answer-option" type="button">
          <span class="answer-badge">
            <svg width="48" height="48" viewBox="0 0 48 48" aria-hidden="true">
              <circle cx="24" cy="24" r="21" fill="none" stroke="var(--white)" stroke-width="3"/>
              <path d="M14 25 L21 32 L34 17" fill="none" stroke="var(--white)" stroke-width="3.2" stroke-linecap="round" stroke-linejoin="round"/>
            </svg>
          </span>
          <span class="answer-label">Yes</span>
        </button>
        <button class="answer-option" type="button">
          <span class="answer-badge">
            <svg width="44" height="44" viewBox="0 0 44 44" aria-hidden="true">
              <circle cx="22" cy="22" r="19" fill="none" stroke="var(--white)" stroke-width="3"/>
              <path d="M15.5 15.5 L28.5 28.5 M28.5 15.5 L15.5 28.5" stroke="var(--white)" stroke-width="3" stroke-linecap="round"/>
            </svg>
          </span>
          <span class="answer-label">No</span>
        </button>
      </div>
    </section>
  </main>

  <footer class="site-footer">
    <span>Copyrights @ 2017 Plum Rivet. All Rights Reserved.</span>
    <span class="page-code">C20</span>
  </footer>
</body>
</html>
```